Business Card Design Project

TRX Solutions is a Electrical and Communications Services and Maintenance contractor to the Mining Oil and Gas sectors of Australia.
Our clients will be planners, Schedulers, Tradespeople and Engineers

We are yet to determine the primary colours that we will use on the business cards but the logos attached will form foundation of the colours used for logos on Business cards, Website, Uniforms, vehicles etc.

Target Market(s)

Mining engineers and shedulers

Industry/Entity Type

Contractor

Requirements
Must have
• information to be included on the card

Name: Derek Hanley
Title: Managing Director
Company: TRX Solutions Pty Ltd
Phone: 08 9XXX XXXX
Mobile 0400 318 942
email: dhanley@trxsolutionsgroup.com.au
Website www.trxsolutionsgroup.com.au

Address: U5/14 Kettering Street Bayswater, WA 6053
Postal Address: PO Box 7183 Bayswater WA 6933

Nice to have
• Double sided. Maybe the logo on the back

```html
<!DOCTYPE html>
<html lang="en">
<head>
<meta charset="utf-8">
<title>TRX Solutions – Business Card</title>
<link rel="stylesheet" href="https://fonts.googleapis.com/css2?family=Exo+2:wght@400;600&display=swap">
<style>
  :root {
    --backdrop: #dcdcdc;
    --card: #2e2e2e;
    --card-edge: #3a3a3a;
    --text-strong: #e6e6e6;
    --text-soft: #b9b9b9;
    --accent: #f07c22;
    --rule: #8a8a8a;
  }
  * { margin: 0; padding: 0; box-sizing: border-box; }
  html, body {
    width: 1200px; height: 857px; overflow: hidden;
    background: var(--backdrop);
    font-family: "Exo 2", sans-serif;
  }
  .sheet { position: relative; width: 1200px; height: 857px; }
  .card {
    position: absolute; left: 300px;
    width: 600px; height: 340px;
    background: var(--card);
    border: 1px solid var(--card-edge);
    border-radius: 38px;
    box-shadow: 0 6px 18px rgba(0,0,0,0.25);
    color: var(--text-soft);
  }
  .card--front { top: 48px; }
  .card--back  { top: 468px; }

  .wordmark {
    position: absolute;
    color: var(--text-strong);
    font-weight: 400; font-size: 46px; letter-spacing: 1px; line-height: 1;
    white-space: nowrap;
  }
  .card--front .wordmark { left: 78px; top: 100px; }
  .card--back .wordmark { left: 50%; top: 132px; transform: translateX(-50%); }

  .holder {
    position: absolute; right: 272px; top: 264px;
    text-align: right; font-size: 11px; line-height: 16px;
  }
  .holder__name { color: var(--text-strong); font-weight: 600; }

  .divider {
    position: absolute; left: 342px; top: 236px;
    width: 1px; height: 56px; background: var(--rule);
  }

  .contact {
    position: absolute; left: 357px; top: 236px;
    font-size: 11px; line-height: 14.5px; white-space: nowrap;
  }
  .contact__company { color: var(--text-strong); font-weight: 600; }
  .contact__label { color: var(--text-strong); font-weight: 600; }
  .contact__web { color: var(--accent); letter-spacing: 1.5px; }

  .address {
    position: absolute; right: 48px; bottom: 52px;
    text-align: right; font-size: 11px; line-height: 15px; white-space: nowrap;
  }
</style>
</head>
<body>
<main class="sheet">
  <section class="card card--front" aria-label="Card front">
    <div class="wordmark">TRX Solutions</div>
    <div class="holder">
      <p class="holder__name">Derek Hanley</p>
      <p class="holder__title">Managing Director</p>
    </div>
    <div class="divider"></div>
    <div class="contact">
      <p class="contact__company">TRX Solutions Pty Ltd</p>
      <p><span class="contact__label">P</span> 08 9XXX XXXX&nbsp; <span class="contact__label">M</span> 0400 318 942</p>
      <p>dhanley@trxsolutionsgroup.com.au</p>
      <p class="contact__web">www.trxsolutionsgroup.com.au</p>
    </div>
  </section>

  <section class="card card--back" aria-label="Card back">
    <div class="wordmark">TRX Solutions</div>
    <div class="address">
      <p>Address: U5/14 Kettering Street Bayswater, WA 6053</p>
      <p>Postal Address: PO Box 7183 Bayswater WA 6933</p>
    </div>
  </section>
</main>
</body>
</html>
```